Bench Advertisement - We Buy Houses Design Needed

Need a catchy, simple but elegant design for bus benches to advertise our company.

We need our website, or phone number, and a smal description (1-2 bulletpoints of what we do and what we offer)

The tricky part is for the designer to fit everything and make the website name as part of the title and fitting everything so that people passing by on the street can see what we offer.

Our website is quickhomeofferhub.com - (916) 555-0142

Something simple but something that catches the eye of walking pedestrians, and drivers driving by the bench.

Our company buys houses, any condition, any situation, we buy houses for cash and close quickly. You can use this description to create a few bulletpoints however you like. Must follow dimensions in attachment.

Target Market(s)

People in foreclosure, about to lose their homes, people that need a quick cash sale of their property

Industry/Entity Type

Real Estate

Requirements
Must have
• catchy, website name, phone number, few brief bulletpoints about what we offer, colors that will catch peoples eye while walking or driving - advertisement will be placed on bus benches - visit our website to see the type of houses we buy - Also have more work for winner of design with possible bonuses
Nice to have
• Feel free to use description or images on our website - make sure the description is just bullet points and it fits with the overall theme / size of the advertisement - Bold bright colors - put yourself in their shoes (if you were going through financial difficulties and about to lose your house to foreclosure or auction, what would you want to see to pick up the phone and call us for a quick sale of your house?) (or if you have a house that you are having a problem with, problem renters, unkept/beat up house, what would make you want to call us and sell your house to us?)

```html
<!DOCTYPE html>
<html lang="en">
<head>
<meta charset="utf-8">
<title>Quick Home Offer Hub – Bench Advertisement</title>
<link rel="stylesheet" href="https://fonts.googleapis.com/css2?family=PT+Sans&family=Oswald:wght@300;400&display=swap">
<style>
  :root {
    --page-bg: #ecebe8;
    --teal: #17807c;
    --teal-deep: #126d6a;
    --panel: #93bcb9;
    --panel-soft: #a9cac8;
    --frame: #f3f7f6;
    --ink-light: #ffffff;
    --ink-teal: #136e6c;
  }
  * { box-sizing: border-box; margin: 0; padding: 0; }
  html, body { width: 1200px; height: 1061px; overflow: hidden; background: var(--page-bg); }
  .ad-card {
    position: absolute; left: 50px; top: 270px; width: 1100px; height: 520px;
    background: linear-gradient(180deg, var(--teal) 0%, var(--teal) 70%, var(--teal-deep) 100%);
    box-shadow: 0 14px 30px rgba(0,0,0,0.18);
    overflow: hidden;
  }
  .ad-heading {
    position: absolute; top: 34px; left: 0; right: 0; text-align: center;
    font-family: "PT Sans", sans-serif; font-weight: 400; font-size: 36px; line-height: 1.2;
    color: var(--ink-light);
  }
  .info-panel {
    position: absolute; left: 30px; right: 30px; top: 110px; height: 330px;
    background: linear-gradient(90deg, var(--panel) 0%, var(--panel-soft) 50%, var(--panel) 100%);
    overflow: hidden;
  }
  .info-frame {
    position: absolute; inset: 14px; border: 2px solid var(--frame);
  }
  .house-decor {
    position: absolute; bottom: 16px;
    background: linear-gradient(180deg, rgba(23,128,124,0.08), rgba(23,128,124,0.24));
  }
  .house-decor--left { left: 30px; width: 200px; height: 160px; }
  .house-decor--right { right: 30px; width: 300px; height: 260px; }
  .info-content {
    position: absolute; inset: 16px; display: flex; flex-direction: column; align-items: center;
    justify-content: center; text-align: center;
  }
  .brand-name {
    font-family: "Oswald", sans-serif; font-weight: 400; font-size: 17px; line-height: 1.3;
    letter-spacing: 1px; color: var(--ink-teal); display: flex; align-items: center; gap: 8px;
  }
  .brand-mark { width: 12px; height: 12px; background: var(--ink-teal); }
  .website {
    margin-top: 4px; font-family: "Oswald", sans-serif; font-weight: 400; font-size: 58px;
    line-height: 1.1; color: var(--ink-light);
  }
  .phone {
    margin-top: 2px; display: flex; align-items: center; gap: 12px;
    font-family: "Oswald", sans-serif; font-weight: 400; font-size: 36px; line-height: 1.25;
    color: var(--ink-teal);
  }
  .phone svg { width: 32px; height: 32px; }
  .offer-list { list-style: none; margin-top: 8px; }
  .offer-list li {
    font-family: "Oswald", sans-serif; font-weight: 300; font-size: 28px; line-height: 1.3;
    color: var(--ink-light); display: flex; align-items: center; justify-content: center; gap: 14px;
  }
  .offer-list svg { width: 12px; height: 22px; }
</style>
</head>
<body>
  <section class="ad-card">
    <h1 class="ad-heading">Just Look at on Green Area</h1>
    <div class="info-panel">
      <div class="house-decor house-decor--left" role="img" aria-label="Faint house silhouettes decoration"></div>
      <div class="house-decor house-decor--right" role="img" aria-label="Faint house silhouettes decoration"></div>
      <div class="info-frame"></div>
      <div class="info-content">
        <p class="brand-name"><span class="brand-mark"></span>QUICK HOME OFFER HUB</p>
        <p class="website">quickhomeofferhub.com</p>
        <p class="phone">
          <svg viewBox="0 0 34 34" aria-hidden="true">
            <circle cx="17" cy="17" r="15" fill="none" stroke="currentColor" stroke-width="2.5"/>
            <path d="M12 9c1 0 2 3 2 4s-2 1-1 3 3 4 5 5 2-1 3-1 4 1 4 2-2 3-3 3c-4 0-12-7-12-12 0-2 1-4 2-4z" fill="currentColor"/>
          </svg>
          (916) 555-0142
        </p>
        <ul class="offer-list">
          <li><svg viewBox="0 0 12 22" aria-hidden="true"><path d="M2 2l8 9-8 9" fill="none" stroke="#136e6c" stroke-width="4"/></svg>We buy houses for cash and close quickly</li>
          <li><svg viewBox="0 0 12 22" aria-hidden="true"><path d="M2 2l8 9-8 9" fill="none" stroke="#136e6c" stroke-width="4"/></svg>Our company buys houses, any condition, any situation</li>
        </ul>
      </div>
    </div>
  </section>
</body>
</html>
```